Stationery Design Project

Hi All,

We need you to design stationary for a new Business and Accounting Advisory Firm. We have already got the logo designed and it is attached. If you could also if possible, match the fonts in your design to that on the logo’s provided.

What we need:
- Business Card
- A4 Letter head
- A4 Folders
- PPT template (Title page and regular page)

And what ever else you want to throw in.

We are in the process of getting the web site designed, however below is a list of websites which we like which will give you an understanding of the style that we are going for.

- plavoni.com
- brightfunnelo.com
- hourquillet.com
- artmarrowly.com

I look forward to your seeing your design.

Hi All,

I have just realised that I forgot that i need to include a Licensed Tallymasters image on the letter head, please find attaced as File 1. Could you please have this image in the bottom left header.

Regards,

Gareth

Industry/Entity Type

Business

Requirements
Must have
• Outputs:
- Documents ready to print
- Generic editable information
- Pdf copies of the documents
- Word version of letterhead

```html
<!DOCTYPE html>
<html lang="en">
<head>
<meta charset="utf-8">
<title>Tarrant Partners – Business Card</title>
<link href="https://fonts.googleapis.com/css2?family=EB+Garamond:wght@500&family=Arimo:wght@400&display=swap" rel="stylesheet">
<style>
  :root {
    --page-bg: #e4e4e4;
    --card-front: #f4f5f7;
    --card-back: #ffffff;
    --card-edge: #d6d6d6;
    --brand-blue: #3a5a98;
    --accent-orange: #f39a1e;
    --text-grey: #5a5a5a;
  }
  html, body {
    margin: 0;
    padding: 0;
    width: 1200px;
    height: 1000px;
    overflow: hidden;
    background: var(--page-bg);
  }
  .canvas {
    position: relative;
    width: 1200px;
    height: 1000px;
  }
  .card {
    position: absolute;
    left: 275px;
    width: 646px;
    height: 323px;
    box-sizing: border-box;
    border: 1px solid var(--card-edge);
  }
  .card--front {
    top: 138px;
    background: var(--card-front);
  }
  .card--back {
    top: 530px;
    background: var(--card-back);
    font-family: "Arimo", Arial, sans-serif;
    font-size: 18px;
    color: var(--text-grey);
    line-height: 24px;
  }
  .brand {
    position: absolute;
    left: 0;
    right: 0;
    top: 122px;
    display: flex;
    justify-content: center;
    align-items: center;
    gap: 16px;
  }
  .brand__square {
    width: 44px;
    height: 44px;
    background: var(--brand-blue);
  }
  .brand__name {
    font-family: "EB Garamond", Garamond, serif;
    font-weight: 500;
    font-size: 40px;
    color: var(--brand-blue);
    line-height: 1;
  }
  .website {
    position: absolute;
    left: 45px;
    top: 36px;
    color: var(--accent-orange);
  }
  .address {
    position: absolute;
    left: 373px;
    top: 36px;
    margin: 0;
    font-style: normal;
  }
  .contacts {
    position: absolute;
    left: 340px;
    top: 178px;
    margin: 0;
    display: grid;
    grid-template-columns: 34px auto;
    row-gap: 3.5px;
  }
  .contacts dt {
    color: var(--accent-orange);
  }
  .contacts dd {
    margin: 0;
  }
</style>
</head>
<body>
  <main class="canvas">
    <section class="card card--front" aria-label="Business card front">
      <div class="brand">
        <span class="brand__square"></span>
        <span class="brand__name">Tarrant Partners</span>
      </div>
    </section>

    <section class="card card--back" aria-label="Business card back">
      <div class="website">www.xxxxxxx.com.au</div>
      <address class="address">14 Lorem Street, Aenean<br>Anriean VIC 3000</address>
      <dl class="contacts">
        <dt>t</dt><dd>03 000 000</dd>
        <dt>f</dt><dd>03 000 000</dd>
        <dt>m</dt><dd>0400 000 000</dd>
        <dt>e</dt><dd>xxxxx@xxxxxx.com.au</dd>
      </dl>
    </section>
  </main>
</body>
</html>
```